Corinne Dabney Interiors business cards

We need a DOUBLE SIDED business card design that is simple, elegant and modern. We are a rapidly growing Interior Design Firm, and our brand colours are blush pink, navy, and antique gold, so we require some or all of these colours to be used. The final design should portray elegance, simplicity, and have a modern feel. We have upload inspiration photos that have the feel we're looking for.

Industry/Entity Type

Interior Design

Contact Information for Business Card

Contact information and LOGO

Colors
EB3D1F
EC4F4E
F09395
F8D3D4
FCEDEE

Requirements
Must have
• Navy, the right shade of blush pink, and antique gold

```html
<!DOCTYPE html>
<html lang="en">
<head>
<meta charset="utf-8">
<title>Corinne Dabney Interiors — Business Cards</title>
<link href="https://fonts.googleapis.com/css2?family=Open+Sans:wght@400;600;700;800&display=swap" rel="stylesheet">
<style>
  :root {
    --blush: #fcedee;
    --navy: #1f275a;
    --coral: #ea504e;
    --gold: #9a7b4f;
    --stage: #ffffff;
  }
  * { margin: 0; padding: 0; box-sizing: border-box; }
  html, body {
    width: 1200px; height: 900px; overflow: hidden;
    background: var(--stage);
    font-family: "Open Sans", Arial, sans-serif;
  }
  .card {
    position: absolute; left: 262px;
    width: 675px; height: 405px;
    background: var(--blush);
    box-shadow: -6px 6px 10px rgba(0,0,0,0.28);
    overflow: hidden;
  }
  .card--front { top: 24px; }
  .card--back { top: 471px; }
  .card__shapes { position: absolute; inset: 0; width: 100%; height: 100%; }
  .wordmark {
    position: absolute;
    color: var(--gold);
    font-weight: 400;
    text-transform: uppercase;
    white-space: nowrap;
    transform: translateX(-50%);
  }
  .card--front .wordmark { left: 187px; top: 212px; font-size: 15px; letter-spacing: 0.5px; }
  .card--back .wordmark { left: 563px; top: 126px; font-size: 11.5px; letter-spacing: 0.3px; }
  .holder { position: absolute; left: 49px; top: 103px; color: var(--navy); }
  .holder__name { font-weight: 800; font-size: 27px; line-height: 1; letter-spacing: 0.2px; }
  .holder__title { font-weight: 700; font-size: 16px; line-height: 1; margin-top: 5px; margin-left: 2px; }
  .holder__rule { display: flex; width: 205px; height: 3px; margin-top: 9px; margin-left: 2px; }
  .holder__rule span { flex: 1; }
  .rule--coral { background: var(--coral); }
  .rule--navy { background: var(--navy); }
  .rule--gold { background: var(--gold); }
  .contacts { position: absolute; left: 49px; top: 233px; list-style: none; color: var(--navy); }
  .contacts li { display: flex; align-items: center; height: 26px; font-size: 16.5px; }
  .contacts svg { width: 18px; height: 18px; margin-right: 9px; flex: none; }
</style>
</head>
<body>

<section class="card card--front">
  <svg class="card__shapes" viewBox="0 0 675 405" aria-hidden="true">
    <polygon points="338,0 675,0 675,405 460,405 543,242" fill="var(--gold)"/>
    <polygon points="351,0 664,0 547,230" fill="var(--navy)"/>
    <polygon points="675,9 675,405 470,405" fill="var(--coral)"/>
  </svg>
  <p class="wordmark">Corinne Dabney Interiors</p>
</section>

<section class="card card--back">
  <svg class="card__shapes" viewBox="0 0 675 405" aria-hidden="true">
    <polygon points="338,247 464,322 675,198 675,405 338,405" fill="var(--gold)"/>
    <polygon points="338,258 458,328 338,402" fill="var(--navy)"/>
    <polygon points="675,212 675,405 352,405" fill="var(--coral)"/>
  </svg>

  <div class="holder">
    <h1 class="holder__name">CORINNE DABNEY</h1>
    <p class="holder__title">PRINCIPAL DESIGNER</p>
    <div class="holder__rule"><span class="rule--coral"></span><span class="rule--navy"></span><span class="rule--gold"></span></div>
  </div>

  <ul class="contacts">
    <li>
      <svg viewBox="0 0 24 24" aria-hidden="true"><path d="M6.6 3.5l2.7 3.6-1.6 2.2c1 2.3 2.8 4.2 5.1 5.3l2.2-1.6 3.6 2.7-1.4 3.3c-6.9-.4-12.4-5.9-12.9-12.8z" fill="var(--coral)"/><path d="M14 4.5a6 6 0 0 1 5.5 5.5M14 1.5a9 9 0 0 1 8.5 8.5" stroke="var(--coral)" stroke-width="1.6" fill="none"/></svg>
      905 555 0142
    </li>
    <li>
      <svg viewBox="0 0 24 24" aria-hidden="true"><circle cx="12" cy="12" r="4" stroke="var(--coral)" stroke-width="2.4" fill="none"/><path d="M16 8v5.5a2.5 2.5 0 0 0 5 0V12a9 9 0 1 0-3.6 7.2" stroke="var(--coral)" stroke-width="2.4" fill="none"/></svg>
      corinne@cdinteriorsinc.com
    </li>
    <li>
      <svg viewBox="0 0 24 24" aria-hidden="true"><circle cx="12" cy="12" r="9.5" stroke="var(--coral)" stroke-width="2" fill="none"/><path d="M2.5 12h19M12 2.5v19M12 2.5c-3.5 4-3.5 15 0 19M12 2.5c3.5 4 3.5 15 0 19" stroke="var(--coral)" stroke-width="1.6" fill="none"/></svg>
      www.corinnedabneyinteriors.com
    </li>
  </ul>

  <p class="wordmark">Corinne Dabney Interiors</p>
</section>

</body>
</html>
```